New Innovative Counselling and psychotherapy Service needs Business Card design

Keep it simple and professional. On one side, just company name and logo (perhaps in all blue) and maybe a tag line.

On other side (all white) my name and Qualifications in centre

Industry/Entity Type

Health And Wellness

Contact Information for Business Card

Derek Hollis
Counsellor & Psychotherapist
BSc (Psychol.), BA, Dip. (Couns. & Psych.), PG.Cert (CBT), MGVrA, NWTF

I will also require Mobile no, Email and web site address of which I'll pass on to final designer.

Font styles to use
Sans Serif

Requirements
Must have
• My Logo Only and please use the colours in logo that is in it.
Should not have
• Any other images

```html
<!DOCTYPE html>
<html lang="en">
<head>
<meta charset="utf-8">
<title>Harbor Grove – Business Card</title>
<link href="https://fonts.googleapis.com/css2?family=Lato:ital,wght@0,300;0,400;0,700;1,700&display=swap" rel="stylesheet">
<style>
  :root {
    --brand-blue: #4fb1e3;
    --brand-green: #98cb5c;
    --ink: #2b2b2b;
    --paper: #ffffff;
    --stage: #e4e5e7;
    --faint-blue: #eef6fc;
  }
  * { box-sizing: border-box; margin: 0; padding: 0; }
  html, body {
    width: 1200px; height: 442px; overflow: hidden;
    background: var(--stage);
    font-family: "Lato", sans-serif;
  }
  .card {
    position: absolute; top: 70px;
    width: 523px; height: 300px;
    background: var(--paper);
    overflow: hidden;
  }
  .card--front { left: 69px; }
  .card--back { left: 608px; }

  .brand {
    position: absolute; display: flex; align-items: center;
  }
  .brand__dot { border-radius: 50%; background: var(--brand-blue); flex: none; }
  .brand__name { font-weight: 300; color: var(--ink); white-space: nowrap; }

  .card--front .brand { left: 37px; top: 44px; gap: 22px; }
  .card--front .brand__dot { width: 60px; height: 60px; }
  .card--front .brand__name { font-size: 28px; }

  .backdrop-circle {
    position: absolute; left: 362px; top: 2px;
    width: 150px; height: 150px; border-radius: 50%;
    background: var(--faint-blue);
  }

  .holder { position: absolute; left: 36px; top: 188px; }
  .holder__name { font-size: 23px; font-weight: 700; color: var(--brand-blue); line-height: 1.1; }
  .holder__role { font-size: 11px; font-weight: 700; font-style: italic; color: var(--ink); margin-top: 6px; }

  .credentials-band {
    position: absolute; left: 0; top: 237px; width: 300px; height: 35px;
    background: var(--brand-blue);
  }
  .credentials {
    position: absolute; left: 36px; top: 241px;
    font-size: 10px; line-height: 13px; color: var(--paper);
  }

  .contact-panel { position: absolute; left: 0; top: 0; width: 523px; height: 300px; }

  .contact-list {
    position: absolute; left: 324px; top: 199px; list-style: none;
  }
  .contact-list li {
    display: flex; align-items: center; gap: 10px;
    height: 20px; margin-bottom: 3.5px;
    font-size: 11px; color: var(--paper);
  }
  .contact-icon {
    width: 20px; height: 20px; border-radius: 50%;
    background: var(--paper); display: flex; align-items: center; justify-content: center;
  }

  .card--back .brand {
    left: 0; right: 0; top: 52px; flex-direction: column; gap: 24px;
  }
  .card--back .brand__dot { width: 136px; height: 136px; }
  .card--back .brand__name { font-size: 29px; letter-spacing: 0.5px; }
</style>
</head>
<body>

<section class="card card--front">
  <div class="backdrop-circle" aria-hidden="true"></div>

  <div class="brand">
    <span class="brand__dot" aria-hidden="true"></span>
    <span class="brand__name">Harbor Grove</span>
  </div>

  <div class="holder">
    <h1 class="holder__name">Derek Hollis</h1>
    <p class="holder__role">Counsellor &amp; Psychotherapist</p>
  </div>

  <div class="credentials-band" aria-hidden="true"></div>

  <svg class="contact-panel" viewBox="0 0 523 300" aria-hidden="true">
    <polygon points="295,189 523,189 523,282 261,282" fill="var(--brand-green)"/>
  </svg>

  <p class="credentials">BSc (Psychol.), BA, Dip. (Couns. &amp; Psych.),<br>PG.Cert (CBT), MGVrA, NWTF</p>

  <ul class="contact-list">
    <li>
      <span class="contact-icon">
        <svg width="12" height="12" viewBox="0 0 12 12"><rect x="3" y="1" width="6" height="10" rx="1" fill="none" stroke="var(--brand-green)" stroke-width="1.2"/><line x1="5" y1="9.3" x2="7" y2="9.3" stroke="var(--brand-green)"/></svg>
      </span>
      000 0000 0000
    </li>
    <li>
      <span class="contact-icon">
        <svg width="12" height="12" viewBox="0 0 12 12"><rect x="1.5" y="3" width="9" height="6.5" fill="none" stroke="var(--brand-green)" stroke-width="1.1"/><polyline points="1.5,3 6,7 10.5,3" fill="none" stroke="var(--brand-green)" stroke-width="1.1"/></svg>
      </span>
      hello@harborgrove.com
    </li>
    <li>
      <span class="contact-icon">
        <svg width="12" height="12" viewBox="0 0 12 12"><circle cx="6" cy="6" r="4.6" fill="none" stroke="var(--brand-green)" stroke-width="1.1"/><ellipse cx="6" cy="6" rx="2" ry="4.6" fill="none" stroke="var(--brand-green)" stroke-width="1"/><line x1="1.4" y1="6" x2="10.6" y2="6" stroke="var(--brand-green)"/></svg>
      </span>
      harborgrove.com
    </li>
  </ul>
</section>

<section class="card card--back">
  <div class="brand">
    <span class="brand__dot" aria-hidden="true"></span>
    <span class="brand__name">Harbor Grove</span>
  </div>
</section>

</body>
</html>
```